Luminously Grounded Vitality

We want to design a business card that is modern and appealing for an innovative psychedelic telemedicine company that provides at-home ketamine-assisted therapy along with wellness, longevity, and anti-aging medicines. We want to use our deep purple and white plus other colors you can find on our website. We don't have any strict brand guidelines yet so feel free to get creative. We want a very professional, but technology first modern design that will instill trust, peace, calm, but also be attractive to investors in the healthcare and SaaS space.

```html
<!DOCTYPE html>
<html lang="en">
<head>
<meta charset="utf-8">
<title>Luminously Grounded Vitality – Business Card</title>
<link rel="stylesheet" href="https://fonts.googleapis.com/css2?family=Montserrat:wght@400;500;600&family=Arimo&display=swap">
<style>
  :root {
    --paper: #fefdf0;
    --navy: #22215f;
    --wordmark: #b07aaa;
    --mark: #8a6fb3;
    --ink: #2e2d8a;
    --name: #22215f;
    --title: #a3238f;
    --white: #ffffff;
  }
  * { margin: 0; padding: 0; box-sizing: border-box; }
  html, body { width: 1199px; height: 1200px; overflow: hidden; background: var(--paper); }
  .canvas { position: relative; width: 1199px; height: 1200px; }
  .card {
    position: absolute; left: 261px; width: 676px; height: 429px; overflow: hidden;
    box-shadow: 0 18px 16px -12px rgba(90, 88, 70, 0.35);
  }
  .card--front { top: 132px; background: var(--white); }
  .card--back { top: 638px; background: var(--navy); }
  .card__field { position: absolute; inset: 0; width: 100%; height: 100%; }

  .brand__dot { position: absolute; border-radius: 50%; }
  .brand__name { position: absolute; transform: translateX(-50%); font-family: "Montserrat", sans-serif; font-weight: 400; white-space: nowrap; }

  .card--front .brand__dot { left: 400px; top: 58px; width: 88px; height: 88px; background: var(--mark); }
  .card--front .brand__name { left: 444px; top: 194px; font-size: 24px; color: var(--wordmark); }

  .person { position: absolute; left: 444px; top: 266px; transform: translateX(-50%); text-align: center; }
  .person__name { font-family: "Montserrat", sans-serif; font-weight: 600; font-size: 24px; letter-spacing: 0.5px; color: var(--name); text-decoration: underline; text-decoration-thickness: 2px; text-underline-offset: 0px; line-height: 1; white-space: nowrap; }
  .person__title { margin-top: 4px; font-family: "Montserrat", sans-serif; font-weight: 500; font-size: 11px; letter-spacing: 0.6px; color: var(--title); }

  .contact { position: absolute; display: flex; align-items: center; font-family: "Arimo", sans-serif; font-size: 15px; color: var(--ink); white-space: nowrap; }
  .contact svg { width: 18px; height: 18px; margin-right: 19px; flex: none; }
  .contact--phone { left: 209px; top: 344px; }
  .contact--web { left: 209px; top: 383px; }
  .contact--email { left: 438px; top: 345px; }
  .contact--email svg { margin-right: 17px; }
  .contact--address { left: 438px; top: 381px; }

  .card--back .brand__dot { left: 284px; top: 70px; width: 96px; height: 96px; background: var(--white); opacity: 0.92; }
  .card--back .brand__name { left: 338px; top: 194px; font-size: 32px; color: var(--white); }
</style>
</head>
<body>
<main class="canvas">

  <section class="card card--front" aria-label="Business card front">
    <svg class="card__field" viewBox="0 0 676 429" preserveAspectRatio="none" role="img" aria-label="Decorative purple and magenta wave area">
      <defs>
        <linearGradient id="front-field" x1="0" y1="0" x2="0.6" y2="1">
          <stop offset="0" stop-color="#231660"/>
          <stop offset="0.55" stop-color="#6a1c78"/>
          <stop offset="1" stop-color="#b4218c"/>
        </linearGradient>
      </defs>
      <path d="M0 0 H320 C230 70 182 160 185 260 C185 320 200 370 222 429 H0 Z" fill="url(#front-field)"/>
    </svg>

    <span class="brand__dot"></span>
    <span class="brand__name">Luminously Grounded Vitality</span>

    <div class="person">
      <p class="person__name">MARA ELLISON</p>
      <p class="person__title">PROJECT MANAGER</p>
    </div>

    <p class="contact contact--phone">
      <svg viewBox="0 0 20 20" aria-hidden="true"><circle cx="10" cy="10" r="8.6" fill="none" stroke="var(--ink)" stroke-width="1.6"/><path d="M7 5.5 L8.6 7.6 L7.8 8.8 C8.4 10.2 9.6 11.4 11 12 L12.2 11.2 L14.3 12.8 L13.3 14.2 C9.5 14 6 10.5 5.8 6.6 Z" fill="var(--ink)"/></svg>
      +1 555 0142
    </p>
    <p class="contact contact--web">
      <svg viewBox="0 0 20 20" aria-hidden="true"><circle cx="10" cy="10" r="8.6" fill="none" stroke="var(--ink)" stroke-width="1.6"/><path d="M1.4 10 H18.6 M10 1.4 C6.5 5 6.5 15 10 18.6 M10 1.4 C13.5 5 13.5 15 10 18.6" fill="none" stroke="var(--ink)" stroke-width="1.2"/></svg>
      www.luminouslyvitality.com
    </p>
    <p class="contact contact--email">
      <svg viewBox="0 0 20 20" aria-hidden="true"><rect x="1.5" y="4.5" width="17" height="11" fill="var(--ink)"/><path d="M1.5 4.5 L10 11 L18.5 4.5 M1.5 15.5 L7.5 9.5 M18.5 15.5 L12.5 9.5" fill="none" stroke="var(--white)" stroke-width="1"/></svg>
      hello@luminouslyvitality.com
    </p>
    <p class="contact contact--address">
      <svg viewBox="0 0 20 20" aria-hidden="true"><path d="M10 1.5 C6.4 1.5 4 4 4 7.4 C4 11.5 10 18.5 10 18.5 C10 18.5 16 11.5 16 7.4 C16 4 13.6 1.5 10 1.5 Z" fill="var(--ink)"/><circle cx="10" cy="7.4" r="2.6" fill="var(--white)"/></svg>
      12 Calm Street
    </p>
  </section>

  <section class="card card--back" aria-label="Business card back">
    <svg class="card__field" viewBox="0 0 676 429" preserveAspectRatio="none" role="img" aria-label="Decorative magenta and violet wave band">
      <defs>
        <linearGradient id="back-field" x1="0" y1="0" x2="1" y2="1">
          <stop offset="0" stop-color="#b01f8a"/>
          <stop offset="0.5" stop-color="#5a1c72"/>
          <stop offset="1" stop-color="#1c1858"/>
        </linearGradient>
      </defs>
      <path d="M0 255 C190 370 440 400 676 255 V429 H0 Z" fill="url(#back-field)"/>
    </svg>

    <span class="brand__dot"></span>
    <span class="brand__name">Luminously Grounded Vitality</span>
  </section>

</main>
</body>
</html>
```